Reaching the Root: Reasoning in Clinical Choice-Making

I'd like a cover that looks like it would fit on the shelf next to "The Symptom Mirage" by Harold Vintner, "The Fall of Forgetting" by Carl Mortenson, "Meal Mend" by Neil Forsby, "The Energy Renewal Plan" by Owen Prichardson or "The Gland Renewal Plan" by the same or "The Cortex Renewal Plan" by the same ... either text only (with some interesting fonts that make the title stand out, and the subtitle smaller) or a relevant image, though I'm not entirely sure what that would be since this is a book about big-picture medical decision making.
Author name is Dr Miriam Oakhurst, NMD
I'll eventually request an e-book, paperback, and audio cover from the winner...

Target Market(s)

practicing physicians

Industry/Entity Type

medicine

Requirements
Must have
• look similar to other books in the genre

```html
<!DOCTYPE html>
<html lang="en">
<head>
<meta charset="utf-8">
<title>Reaching the Root — Book Cover</title>
<link href="https://fonts.googleapis.com/css2?family=Crimson+Pro:wght@400;500&display=swap" rel="stylesheet">
<style>
  :root {
    --backdrop: #03070b;
    --paper: #f5f5f5;
    --ink: #0a0a0a;
    --ink-soft: #231f20;
    --leaf: #97bb3f;
    --rule: #6f8f3a;
    --emblem: #d6d6d6;
  }
  html, body {
    margin: 0;
    padding: 0;
    width: 1200px;
    height: 1200px;
    overflow: hidden;
    background: var(--backdrop);
  }
  .book-cover {
    position: absolute;
    left: 273px;
    top: 109px;
    width: 654px;
    height: 981px;
    display: block;
  }
  .cover-text {
    font-family: "Crimson Pro", "Times New Roman", serif;
  }
  .title-line { fill: var(--ink); font-size: 150px; font-weight: 400; }
  .title-key { fill: var(--leaf); font-size: 196px; font-weight: 400; letter-spacing: 2px; }
  .subtitle { fill: var(--ink-soft); font-size: 29px; letter-spacing: 6px; }
  .author { fill: var(--ink); font-size: 46px; font-weight: 500; }
</style>
</head>
<body>
  <svg class="book-cover" viewBox="0 0 654 981" xmlns="http://www.w3.org/2000/svg" aria-labelledby="cover-title">
    <title id="cover-title">Reaching the Root: Reasoning in Clinical Choice-Making by Dr Miriam Oakhurst, NMD</title>
    <rect class="cover-paper" x="0" y="0" width="654" height="981" fill="var(--paper)"/>

    <g class="cover-text">
      <text class="title-line" x="327" y="195" text-anchor="middle">Reaching</text>
      <text class="title-line" x="327" y="329" text-anchor="middle">the</text>
      <text class="title-key" x="327" y="515" text-anchor="middle">ROOT</text>
    </g>

    <polygon class="maze-emblem" role="img" aria-label="Faint grey hexagonal labyrinth emblem"
      points="326,537 466,612 466,782 326,857 187,782 187,612"
      fill="var(--emblem)" opacity="0.55"/>

    <line class="subtitle-rule" x1="82" y1="633" x2="593" y2="633" stroke="var(--rule)" stroke-width="0.8"/>
    <line class="subtitle-rule" x1="82" y1="757" x2="593" y2="757" stroke="var(--rule)" stroke-width="0.8"/>

    <g class="cover-text">
      <text class="subtitle" x="340" y="687" text-anchor="middle">REASONING IN CLINICAL</text>
      <text class="subtitle" x="340" y="734" text-anchor="middle">CHOICE-MAKING</text>
    </g>

    <rect class="author-band" x="0" y="867" width="654" height="114" fill="var(--leaf)"/>
    <text class="cover-text author" x="327" y="940" text-anchor="middle">Dr Miriam Oakhurst, NMD</text>
  </svg>
</body>
</html>
```